Film Poster For Short Thriller

UPDATE:

The original concept seemed to be a bit difficult for designers to source elements, so we're changing our brief.

Please use the biohazard symbol (attached for reference only, please use any source file for this symbol you would like) in the middle of the poster. In the top 1/3 please place "Plim" in large font with "A Doran Kelvitch Film" in smaller font underneath it. All text should be centered.

What we would like to see with this simplified design is something that's eye-catching but simple and elegant. There should be interesting detail (e.g. texture added to the biohazard symbol, an interesting but not distracting background).

What the design is and what it needs is extremely simple and fully laid out above. We're looking for someone who can take a simple idea (which on the face of it is also simple to execute) and add something memorable. Thank you!
Updates

Hello all, and thank you for your interest in this project. It seems that the original brief was difficult to execute without better source images. The brief has been updated in a way that we believe will be much easier for graphic designers to create an impactful poster. Thank you!

Target Market(s)

Film festivals, online promotion, Strella Reel On Demand

Colors
0255a3
fbee3e

Requirements
Must have
• The dimensions will be 24” width, 40” height, and high enough PPI to be printed at that size. I would think that would 300 PPI, but if you have other thoughts please let me know.

```html
<!DOCTYPE html>
<html lang="en">
<head>
<meta charset="utf-8">
<title>Plim — A Doran Kelvitch Film</title>
<link rel="stylesheet" href="https://fonts.googleapis.com/css2?family=Michroma&family=Montserrat:wght@500&display=swap">
<style>
  :root {
    --night: #0b1c24;
    --deep-teal: #163d48;
    --mist-teal: #5f8f95;
    --glow-warm: #fff6dc;
    --glow-gold: #d9c18a;
    --chrome-light: #f4f6f4;
    --chrome-mid: #b9c2bf;
    --chrome-dark: #5b6663;
    --credit-grey: #d5dcdc;
  }
  html, body {
    margin: 0;
    padding: 0;
    width: 720px;
    height: 1200px;
    overflow: hidden;
    background: var(--night);
  }
  .poster {
    position: relative;
    width: 720px;
    height: 1200px;
    overflow: hidden;
    background:
      radial-gradient(ellipse 60% 42% at 50% 43%, rgba(255,246,220,0.55) 0%, rgba(217,193,138,0.25) 30%, rgba(95,143,149,0.18) 55%, rgba(11,28,36,0) 80%),
      radial-gradient(ellipse 90% 70% at 50% 45%, var(--deep-teal) 0%, var(--night) 85%);
  }
  .poster__rays {
    position: absolute;
    inset: 0;
    width: 720px;
    height: 1200px;
  }
  .credit {
    position: absolute;
    top: 56px;
    left: 0;
    width: 100%;
    margin: 0;
    text-align: center;
    font-family: "Montserrat", sans-serif;
    font-weight: 500;
    font-size: 23px;
    letter-spacing: 3px;
    color: var(--credit-grey);
  }
  .title {
    position: absolute;
    top: 92px;
    left: 0;
    width: 100%;
    margin: 0;
    text-align: center;
    font-family: "Michroma", sans-serif;
    font-weight: 400;
    font-size: 96px;
    line-height: 1.2;
    letter-spacing: 40px;
    padding-left: 40px;
    box-sizing: border-box;
    background: linear-gradient(180deg, var(--chrome-light) 0%, var(--chrome-mid) 45%, var(--chrome-dark) 52%, var(--chrome-light) 100%);
    -webkit-background-clip: text;
    background-clip: text;
    color: transparent;
  }
  .hazard-emblem {
    position: absolute;
    left: 132px;
    top: 288px;
    width: 456px;
    height: 456px;
    border-radius: 50%;
    background: radial-gradient(circle at 50% 50%, var(--glow-warm) 0%, var(--glow-gold) 18%, #8d9794 40%, #4d5a5a 62%, rgba(77,90,90,0) 72%);
  }
</style>
</head>
<body>
  <main class="poster">
    <svg class="poster__rays" viewBox="0 0 720 1200" aria-hidden="true">
      <defs>
        <radialGradient id="ray-fade" cx="360" cy="516" r="620" gradientUnits="userSpaceOnUse">
          <stop offset="0" stop-color="#fff6dc" stop-opacity="0.45"/>
          <stop offset="1" stop-color="#fff6dc" stop-opacity="0"/>
        </radialGradient>
      </defs>
      <g fill="url(#ray-fade)">
        <polygon points="360,516 250,0 300,0"/>
        <polygon points="360,516 420,0 470,0"/>
        <polygon points="360,516 0,230 0,300"/>
        <polygon points="360,516 720,260 720,320"/>
        <polygon points="360,516 0,760 0,830"/>
        <polygon points="360,516 720,720 720,790"/>
        <polygon points="360,516 230,1200 290,1200"/>
        <polygon points="360,516 440,1200 500,1200"/>
        <polygon points="360,516 110,0 150,0"/>
        <polygon points="360,516 600,0 640,0"/>
      </g>
    </svg>

    <p class="credit">A DORAN KELVITCH FILM</p>
    <h1 class="title">PLIM</h1>

    <div class="hazard-emblem" role="img" aria-label="Textured metallic biohazard symbol glowing at the centre of the poster"></div>
  </main>
</body>
</html>
```